Front cover for our tenth anniversary show programme

To create an eye catching tenth anniversary front cover for our programme

Moonbrook presents DANCE! 2015

date of the show Sunday 3rd May 2015

Venue The Harrowgate Stagehouse

please see the updated brief!

Reason: there hasn't been anything that is quite right

```html
<!DOCTYPE html>
<html lang="en">
<head>
<meta charset="utf-8">
<title>Moonbrook presents DANCE! 2015</title>
<link rel="stylesheet" href="https://fonts.googleapis.com/css2?family=Anton&family=Roboto:wght@300;700;900&display=swap">
<style>
  :root {
    --violet-deep: #5a1a9e;
    --violet: #7b2fd0;
    --violet-light: #a66be6;
    --violet-glow: #c58cf2;
    --frame-line: rgba(196, 150, 240, 0.55);
    --pink: #ff3aa2;
    --pink-dark: #c81f7c;
    --pink-shadow: #8e1457;
    --white: #ffffff;
  }
  * { margin: 0; padding: 0; box-sizing: border-box; }
  html, body { width: 848px; height: 1200px; overflow: hidden; background: var(--violet-deep); }
  .cover {
    position: relative;
    width: 848px;
    height: 1200px;
    overflow: hidden;
    background: radial-gradient(ellipse at 50% 50%, var(--violet) 0%, var(--violet-deep) 75%);
    font-family: "Roboto", Arial, sans-serif;
    color: var(--white);
  }
  .photo {
    position: absolute;
    border: 3px solid var(--frame-line);
  }
  .photo--rehearsal { left: -3px; top: -3px; width: 545px; height: 392px;
    background: linear-gradient(160deg, #b583ea 0%, #8d45d6 55%, #6b24b8 100%); }
  .photo--soloist-arms { left: 355px; top: 290px; width: 300px; height: 150px;
    background: linear-gradient(180deg, #a25ee0, #7a30c8); border-top: none; }
  .photo--soloist-gaze { left: 540px; top: 85px; width: 311px; height: 360px;
    background: linear-gradient(200deg, #8a47d4 0%, #6526b2 100%); }
  .photo--ballet-line { left: -3px; top: 385px; width: 360px; height: 310px;
    background: linear-gradient(180deg, #7d34c8 0%, #9a58dc 60%, #6a22b2 100%); }
  .photo--stretch { left: 520px; top: 690px; width: 331px; height: 240px;
    background: linear-gradient(160deg, #7330c2, #5a1a9e); }
  .photo--kneeling { left: -3px; top: 925px; width: 230px; height: 278px;
    background: linear-gradient(170deg, #6a25b4 0%, #4c128a 100%); }
  .photo--young-dancer { left: 225px; top: 940px; width: 355px; height: 263px;
    background: linear-gradient(180deg, #7e3ccb 0%, #9d66dc 50%, #6423ae 100%); }
  .photo--parasols { left: 575px; top: 925px; width: 276px; height: 278px;
    background: linear-gradient(190deg, #a56be0 0%, #7634c2 60%, #561894 100%); }
  .glow {
    position: absolute;
    left: 0; top: 420px; width: 848px; height: 360px;
    background: radial-gradient(ellipse at 50% 55%, rgba(255, 120, 230, 0.45) 0%, rgba(170, 60, 220, 0.25) 45%, rgba(90, 26, 158, 0) 75%);
  }
  .masthead {
    position: absolute;
    left: 0; top: 52px; width: 848px;
    text-align: center;
  }
  .masthead__name {
    font-family: "Roboto", Arial, sans-serif;
    font-weight: 700;
    font-size: 46px;
    line-height: 1;
    color: var(--white);
    display: inline-flex;
    align-items: center;
    gap: 10px;
  }
  .masthead__dot {
    width: 22px; height: 22px; border-radius: 50%;
    background: var(--white);
  }
  .masthead__celebrating {
    margin-top: 14px;
    font-weight: 700;
    font-size: 13px;
  }
  .masthead__years {
    font-weight: 900;
    font-size: 28px;
    line-height: 1.05;
    color: var(--pink);
  }
  .masthead__years span { color: var(--white); }
  .masthead__presents {
    margin-top: 20px;
    font-weight: 300;
    font-size: 22px;
  }
  .title {
    position: absolute;
    left: 0; top: 430px; width: 848px;
    text-align: center;
    font-family: "Anton", Impact, sans-serif;
    font-size: 262px;
    line-height: 1;
    letter-spacing: -2px;
    color: var(--white);
    text-shadow: 8px 8px 0 #3a0e66, 0 0 30px rgba(255, 255, 255, 0.25);
  }
  .ribbon { position: absolute; left: 0; top: 680px; width: 848px; height: 170px; }
  .ribbon__year {
    position: absolute;
    left: 224px; top: 684px; width: 452px; height: 106px;
    display: flex; align-items: center; justify-content: center;
    font-weight: 900;
    font-size: 88px;
    letter-spacing: 18px;
    padding-left: 18px;
    color: var(--white);
  }
  .details {
    position: absolute;
    left: 0; top: 845px; width: 848px;
    text-align: center;
    font-weight: 700;
    font-size: 21px;
    line-height: 29px;
    letter-spacing: 2px;
  }
</style>
</head>
<body>
<main class="cover">
  <div class="photo photo--rehearsal" role="img" aria-label="Photo of young dancers in a rehearsal with arms raised"></div>
  <div class="photo photo--soloist-gaze" role="img" aria-label="Photo of a dancer looking upward on stage"></div>
  <div class="photo photo--ballet-line" role="img" aria-label="Photo of a line of ballet dancers in tutus"></div>
  <div class="photo photo--soloist-arms" role="img" aria-label="Photo of a young soloist with arms outstretched"></div>
  <div class="photo photo--stretch" role="img" aria-label="Photo of a dancer in a floor stretch"></div>
  <div class="photo photo--kneeling" role="img" aria-label="Photo of dancers kneeling in jackets"></div>
  <div class="photo photo--young-dancer" role="img" aria-label="Photo of a young dancer in a leotard"></div>
  <div class="photo photo--parasols" role="img" aria-label="Photo of dancers holding paper parasols"></div>
  <div class="glow"></div>

  <header class="masthead">
    <div class="masthead__name"><span class="masthead__dot"></span>Moonbrook</div>
    <p class="masthead__celebrating">Celebrating</p>
    <p class="masthead__years">Ten <span>Years</span></p>
    <p class="masthead__presents">presents</p>
  </header>

  <h1 class="title">DANCE!</h1>

  <svg class="ribbon" viewBox="0 680 848 170" width="848" height="170" aria-hidden="true">
    <polygon points="94,748 311,738 311,840 94,836 150,790" fill="var(--pink-dark)"/>
    <polygon points="540,738 800,728 750,782 800,836 584,838" fill="var(--pink-dark)"/>
    <polygon points="311,790 311,840 250,790" fill="var(--pink-shadow)"/>
    <polygon points="584,790 584,838 640,790" fill="var(--pink-shadow)"/>
    <rect x="224" y="684" width="452" height="106" fill="var(--pink)"/>
  </svg>
  <p class="ribbon__year">2015</p>

  <p class="details">May 3, 2015, Sunday<br>at The Harrowgate Stagehouse</p>
</main>
</body>
</html>
```